Webesite for sales coach, keynote speaker, blog, author

Business is specifically targeted toward companies looking to optimise the performance of their sales teams with coaching, I would also like this to be a platform for an ongoing blog that will form the content for a book to be written next year. And lastly, as a destination for businesses to learn a little more about me to consider using me as a keynote speaker at their next business event. I need the format of the website to be easy editable by me going forward and ease in adding content and photographs where needed. Some examples of website styles i like include: http://www.brightquillplanner.example , http://marovetka.example/ ,

Target Market(s)

Business Owners

Industry/Entity Type

Business Consultant

Coding

Coded - Design and coding required

Number of Pages Required

1 page

Font styles to use
Serif

Colors

Designer to choose colors to be used in the design.

Requirements
Must have
• Blog functionality (with ability for user to comment), ease of editing and adding new content, striking background photography that drives motivational thoughts (breath-taking landscape photography maybe?)

```html
<!DOCTYPE html>
<html lang="en">
<head>
<meta charset="utf-8">
<title>Harlowmere.com – Sales Coach, Keynote Speaker, Blog Author</title>
<link href="https://fonts.googleapis.com/css2?family=Alegreya+Sans:wght@400;500;700&family=Open+Sans:wght@400;600&display=swap" rel="stylesheet">
<style>
:root{
  --red:#e8262a;
  --ink:#2b2b2b;
  --dark:#333333;
  --muted:#8a8a8a;
  --soft:#f7f7f7;
  --white:#ffffff;
  --line:#dddddd;
}
*{margin:0;padding:0;box-sizing:border-box}
html,body{width:1200px;height:3673px;overflow:hidden}
body{position:relative;background:var(--white);font-family:"Open Sans",Arial,sans-serif;color:var(--ink)}
.abs{position:absolute}
.heading{font-family:"Alegreya Sans",Georgia,serif}

/* header */
.site-header{left:0;top:0;width:1200px;height:127px;background:var(--white)}
.brand{left:98px;top:38px;font-family:"Alegreya Sans",Georgia,serif;font-size:40px;font-weight:500;color:var(--ink)}
.main-nav{left:715px;top:60px;display:flex;gap:0;font-size:13px;letter-spacing:.5px}
.main-nav a{position:absolute;color:#666;text-decoration:none;white-space:nowrap}
.main-nav a.active{color:var(--red)}

/* hero */
.hero{left:0;top:127px;width:1200px;height:530px;background:linear-gradient(180deg,#b7b0a4 0%,#a89a7c 45%,#7d6a2f 75%,#5c5420 100%)}
.hero-title{left:0;top:222px;width:1284px;text-align:center;color:var(--white);font-family:"Alegreya Sans",Georgia,serif;font-size:33px;line-height:44px}
.hero-dots{left:567px;top:466px;display:flex;gap:7px}
.hero-dots span{width:11px;height:11px;border-radius:50%;background:var(--white)}
.hero-dots span.off{background:transparent;border:2px solid var(--white)}

/* about */
.about{left:0;top:657px;width:1200px;height:323px;background:var(--soft)}
.portrait{left:98px;top:527px;width:257px;height:257px;border:7px solid var(--white);box-shadow:0 2px 8px rgba(0,0,0,.2);background:linear-gradient(180deg,#b9c3c8,#8fa5b4)}
.about-lead{left:385px;top:706px;width:720px;font-family:"Alegreya Sans",Georgia,serif;font-size:17px;font-weight:500;line-height:25px;color:var(--ink)}
.about-body{left:385px;top:786px;width:715px;font-size:10px;line-height:20px;color:var(--muted)}
.btn-outline{left:385px;top:894px;width:102px;height:44px;border:1px solid #bbb;background:var(--white);font-size:11px;color:#555;display:flex;align-items:center;justify-content:center}

/* section headings */
.section-title{left:0;width:1200px;text-align:center;font-family:"Alegreya Sans",Georgia,serif;font-size:29px}
.title-swoosh{left:482px;width:240px;height:20px}

/* services */
.service{width:289px;height:331px}
.service svg.hex{position:absolute;left:0;top:0}
.service .icon{position:absolute;left:112px;top:58px}
.service h3{position:absolute;left:0;top:125px;width:289px;text-align:center;font-family:"Alegreya Sans",Georgia,serif;font-weight:500;font-size:18px;color:var(--white)}
.service p{position:absolute;left:40px;top:172px;width:209px;text-align:center;font-size:12px;line-height:21px;color:#e6e6e6}
.service .plus{position:absolute;left:133px;top:276px}

/* blog */
.blog-card{width:289px;height:365px;background:var(--white);box-shadow:0 2px 6px rgba(0,0,0,.12)}
.blog-card .media{position:absolute;left:0;top:0;width:289px;height:186px}
.blog-card .date{position:absolute;left:20px;top:215px;font-size:12px;color:#333}
.blog-card .rule{position:absolute;left:20px;top:240px;width:55px;height:2px;background:var(--red)}
.blog-card .excerpt{position:absolute;left:20px;top:262px;width:250px;font-size:12px;line-height:21px;color:#666}
.blog-card .byline{position:absolute;left:20px;top:325px;font-size:9px;color:#444}
.blog-card .byline b{color:var(--red);font-weight:600}
.share{position:absolute;left:0;top:0;width:289px;height:186px;background:rgba(40,40,40,.55)}
.share small{position:absolute;left:0;top:60px;width:289px;text-align:center;font-size:8px;color:var(--white);letter-spacing:.5px}
.share .row{position:absolute;left:50px;top:85px;display:flex;gap:8px}
.share .row span{width:22px;height:22px;border-radius:50%;border:1px solid #ddd}
.pager{top:2188px;width:24px;height:24px;border-radius:50%}

/* testimonials */
.quote-photo{left:299px;top:2512px;width:162px;height:162px;border-radius:50%;border:5px solid var(--red);background:linear-gradient(180deg,#c9ccd0,#8f9aa4)}
.quote-name{left:502px;top:2522px;font-family:"Alegreya Sans",Georgia,serif;font-size:18px;color:var(--white)}
.quote-text{left:502px;top:2572px;width:395px;font-size:12px;line-height:21px;color:#e8e8e8}
.quote-dots{left:1113px;top:2553px;display:flex;flex-direction:column;gap:12px}
.quote-dots span{width:11px;height:11px;border-radius:50%;background:var(--white)}
.quote-dots span.on{background:var(--red)}

/* newsletter */
.news-sub{left:0;top:2972px;width:1200px;text-align:center;font-size:12px;color:#aaa}
.news-form{left:304px;top:3066px;width:597px;height:71px;display:flex;box-shadow:0 1px 6px rgba(0,0,0,.12)}
.news-form .field{flex:0 0 441px;background:var(--white);font-size:10px;color:#999;padding:0 20px;display:flex;align-items:center}
.news-form .submit{flex:1;background:var(--red);color:var(--white);font-size:12px;font-weight:600;display:flex;align-items:center;justify-content:center}

/* photo feed */
.feed{left:0;top:3198px;width:1200px;height:221px;display:flex}
.feed div{flex:1;position:relative}
.feed-label{position:absolute;left:0;top:128px;width:100%;text-align:center;font-family:"Alegreya Sans",Georgia,serif;font-size:18px;color:var(--white)}
.feed-mark{position:absolute;left:108px;top:97px;width:24px;height:24px;background:var(--red);border-radius:4px}

/* footer */
.footer-brand{left:0;top:3485px;width:1200px;text-align:center;font-family:"Alegreya Sans",Georgia,serif;font-size:38px;font-weight:500;color:var(--ink)}
.footer-social{left:507px;top:3573px;display:flex;gap:12px}
.footer-social span{width:21px;height:21px;border-radius:50%;border:1.5px solid var(--red)}
.copyright{left:0;top:3625px;width:1200px;text-align:center;font-size:10px;color:#333}
</style>
</head>
<body>

<header class="abs site-header">
  <div class="abs brand">Harlowmere.com</div>
  <nav class="abs main-nav" style="left:0;top:60px">
    <a class="active" style="left:715px">HOME</a>
    <a style="left:789px">BIO</a>
    <a style="left:845px">SERVICES</a>
    <a style="left:935px">MEDIA</a>
    <a style="left:1011px">CONTACT</a>
  </nav>
</header>

<section class="abs hero" role="img" aria-label="Photograph of a woman with outstretched arms in a sunlit field of wildflowers"></section>
<h1 class="abs hero-title" style="font-weight:400">Phasellus Nisl Est<br>Condimentum Vitae Faucibus</h1>
<div class="abs hero-dots"><span class="off"></span><span></span><span></span><span></span></div>

<section class="abs about"></section>
<div class="abs portrait" role="img" aria-label="Portrait photograph of the sales coach"></div>
<p class="abs about-lead">Pellentesque blandit lacus eget nunc faucibus, et tincidunt eros viverra. Phasellus consequat sagittis nisi suscipit feugiat. Cras eget leo sed nunc hen drerit ultricies eu at nisl. Fusce eget neque elit.</p>
<p class="abs about-body">Vestibulum condimentum, risus ut posuere cursus, velit justo accumsan sem, lobortis aliquet metus dui eu libero. Pellentesque a imperdiet dolor, et auctor est. Fusce sollicitudin lorem at luctus volutpat. Proin placerat dapibus gravida. In tristique tristique nulla eget hendrerit. Maecenas vel tortor accumsan quam varius imperdiet vel eget elit. Aenean facilisis tincidunt lectus, id dictum nisi luctus eget. Vivamus efficitur ex condimentum, malesuada eros eget, feugiat nibh. Sed tellus ex, imperdiet eget gravida sit amet, volutpat eget turpis. In nec ultricies est.</p>
<div class="abs btn-outline">Read More</div>

<!-- services -->
<h2 class="abs section-title" style="top:1060px;font-weight:400">What We do ?</h2>
<svg class="abs title-swoosh" style="top:1117px" viewBox="0 0 240 20"><path d="M2 16 Q120 -4 238 12" fill="none" stroke="var(--red)" stroke-width="3" stroke-linecap="round"/></svg>

<div class="abs service" style="left:145px;top:1180px">
  <svg class="hex" width="289" height="331"><polygon points="144.5,0 289,83 289,248 144.5,331 0,248 0,83" fill="var(--dark)"/></svg>
  <svg class="icon" width="66" height="56" viewBox="0 0 66 56" fill="none" stroke="#fff" stroke-width="2"><path d="M4 2 V52 H64"/><path d="M8 44 L20 22 L30 36 L40 14 L48 30 L60 10"/></svg>
  <h3>Sales Coach</h3>
  <p>Sed ut perspiciatis unde omnis iste natus error sit voluptatem accusantium doloremque laudantium</p>
  <svg class="plus" width="22" height="22"><circle cx="11" cy="11" r="11" fill="var(--red)"/><path d="M6 11H16M11 6V16" stroke="#fff" stroke-width="2.5"/></svg>
</div>

<div class="abs service" style="left:455px;top:1180px">
  <svg class="hex" width="289" height="331"><polygon points="144.5,0 289,83 289,248 144.5,331 0,248 0,83" fill="var(--red)"/></svg>
  <svg class="icon" width="66" height="56" viewBox="0 0 66 56" fill="none" stroke="#fff" stroke-width="2.5"><rect x="6" y="18" width="12" height="16"/><path d="M18 18 L46 6 V46 L18 34"/><path d="M10 34 L16 50"/><path d="M52 20 H60 M52 26 H62 M52 32 H60"/></svg>
  <h3>keynote Speaker</h3>
  <p>Sed ut perspiciatis unde omnis iste natus error sit voluptatem accusantium doloremque laudantium</p>
  <svg class="plus" width="22" height="22"><circle cx="11" cy="11" r="11" fill="var(--white)"/><path d="M6 11H16M11 6V16" stroke="var(--red)" stroke-width="2.5"/></svg>
</div>

<div class="abs service" style="left:767px;top:1180px">
  <svg class="hex" width="289" height="331"><polygon points="144.5,0 289,83 289,248 144.5,331 0,248 0,83" fill="var(--dark)"/></svg>
  <svg class="icon" width="66" height="56" viewBox="0 0 66 56"><path d="M12 52 C18 30 34 12 58 4 C54 24 40 40 20 44 Z" fill="#fff"/><path d="M10 54 L30 28" stroke="var(--dark)" stroke-width="2"/></svg>
  <h3>Blog Author</h3>
  <p>Sed ut perspiciatis unde omnis iste natus error sit voluptatem accusantium doloremque laudantium</p>
  <svg class="plus" width="22" height="22"><circle cx="11" cy="11" r="11" fill="var(--red)"/><path d="M6 11H16M11 6V16" stroke="#fff" stroke-width="2.5"/></svg>
</div>

<!-- blog background band -->
<svg class="abs" style="left:0;top:1540px" width="1200" height="1310" viewBox="0 0 1200 1310" role="img" aria-label="Soft grey landscape photograph of clouds over a lake behind the blog section">
  <defs>
    <linearGradient id="blogSky" x1="0" y1="0" x2="0" y2="1">
      <stop offset="0" stop-color="#c9c9c9"/><stop offset=".5" stop-color="#ececec"/><stop offset="1" stop-color="#bdbdbd"/>
    </linearGradient>
    <linearGradient id="mountain" x1="0" y1="0" x2="0" y2="1">
      <stop offset="0" stop-color="#5a5a5a"/><stop offset=".6" stop-color="#3e3e3e"/><stop offset="1" stop-color="#575757"/>
    </linearGradient>
  </defs>
  <polygon points="0,78 1200,0 1200,790 0,690" fill="url(#blogSky)"/>
  <polygon points="0,688 1200,788 1200,1300 0,1240" fill="url(#mountain)"/>
</svg>

<h2 class="abs section-title" style="top:1645px;font-weight:400">Blog</h2>
<svg class="abs title-swoosh" style="top:1697px" viewBox="0 0 240 20"><path d="M2 16 Q120 -4 238 12" fill="none" stroke="var(--red)" stroke-width="3" stroke-linecap="round"/></svg>

<article class="abs blog-card" style="left:145px;top:1785px">
  <div class="media" role="img" aria-label="Photograph of a laptop on a desk" style="background:linear-gradient(135deg,#6c6f74,#2f3236)"></div>
  <div class="share"><small>SHARE WITH US</small><div class="row"><span></span><span></span><span></span><span></span><span></span><span></span></div></div>
  <div class="date">July 25th 2017</div><div class="rule"></div>
  <p class="excerpt">Sed ut perspiciatis unde omnis iste natus error sit voluptatem accusantium</p>
  <div class="byline">Posted by <b>Harlowmere</b></div>
</article>
<article class="abs blog-card" style="left:455px;top:1785px">
  <div class="media" role="img" aria-label="Photograph of a team stacking hands over a table" style="background:linear-gradient(135deg,#9aa6ad,#5c6e79)"></div>
  <div class="date">July 25th 2017</div><div class="rule"></div>
  <p class="excerpt">Sed ut perspiciatis unde omnis iste natus error sit voluptatem accusantium</p>
  <div class="byline">Posted by <b>Harlowmere</b></div>
</article>
<article class="abs blog-card" style="left:767px;top:1785px">
  <div class="media" role="img" aria-label="Photograph of colleagues working together in a bright office" style="background:linear-gradient(135deg,#b39a78,#6b5b48)"></div>
  <div class="date">July 25th 2017</div><div class="rule"></div>
  <p class="excerpt">Sed ut perspiciatis unde omnis iste natus error sit voluptatem accusantium</p>
  <div class="byline">Posted by <b>Harlowmere</b></div>
</article>

<svg class="abs pager" style="left:566px" width="24" height="24"><circle cx="12" cy="12" r="12" fill="#bdbdbd"/><path d="M14 7 L9 12 L14 17" fill="none" stroke="#fff" stroke-width="2.5"/></svg>
<svg class="abs pager" style="left:610px" width="24" height="24"><circle cx="12" cy="12" r="12" fill="var(--red)"/><path d="M10 7 L15 12 L10 17" fill="none" stroke="#fff" stroke-width="2.5"/></svg>

<!-- testimonials -->
<h2 class="abs section-title" style="top:2370px;font-weight:400;color:var(--white)">Testimonials</h2>
<svg class="abs title-swoosh" style="top:2422px" viewBox="0 0 240 20"><path d="M2 16 Q120 -4 238 12" fill="none" stroke="var(--red)" stroke-width="3" stroke-linecap="round"/></svg>
<div class="abs quote-photo" role="img" aria-label="Portrait photograph of the client giving the testimonial"></div>
<div class="abs quote-name">Elias Brandt</div>
<p class="abs quote-text">Sed ut perspiciatis unde omnis iste natus error sit voluptatem accusantium doloremque laudantium, totam rem aperiam, eaque ipsa quae ab illo inventore veritatis et quasi architecto beatae vitae dicta sunt explicabo. Nemo enim ipsam volup</p>
<div class="abs quote-dots"><span class="on"></span><span></span><span></span><span></span></div>

<!-- newsletter -->
<h2 class="abs section-title" style="top:2915px;font-weight:500">Newsletter Sign Up</h2>
<p class="abs news-sub">Sed ut perspiciatis unde omnis iste natus error sit voluptatem accus</p>
<svg class="abs title-swoosh" style="top:3007px" viewBox="0 0 240 20"><path d="M2 16 Q120 -4 238 12" fill="none" stroke="var(--red)" stroke-width="3" stroke-linecap="round"/></svg>
<div class="abs news-form"><div class="field">Enter Your E-Mail Address</div><div class="submit">Subscribe Now</div></div>

<!-- photo feed -->
<div class="abs feed">
  <div role="img" aria-label="Dark photograph of a workspace" style="background:linear-gradient(135deg,#4a4a4a,#2a2a2a)"><span class="feed-mark"></span><span class="feed-label">Photo Feed</span></div>
  <div role="img" aria-label="Photograph of businesspeople in a meeting" style="background:linear-gradient(135deg,#c9c4bd,#7d7468)"></div>
  <div role="img" aria-label="Photograph of a laptop on a wooden desk" style="background:linear-gradient(135deg,#8a7058,#3f352c)"></div>
  <div role="img" aria-label="Photograph of hands pointing at papers on a table" style="background:linear-gradient(135deg,#d27a3e,#7a3d1e)"></div>
  <div role="img" aria-label="Photograph of charts and documents on a desk" style="background:linear-gradient(135deg,#d8d8d4,#8d8f92)"></div>
</div>

<!-- footer -->
<footer>
  <div class="abs footer-brand">Harlowmere.com</div>
  <div class="abs footer-social"><span></span><span></span><span></span><span></span><span></span><span></span></div>
  <div class="abs copyright">© 2017 Company Name &nbsp;|&nbsp; All Rights Reserved</div>
</footer>

</body>
</html>
```